Detail Shop Business card design

i need a business card design for my new detailing company called 'Brenner's Detail Shop'. i want an all black and white design . simple, direct and to the point. i want the designer to choose a fitting font to match the logothe front should have logo, address, phone and email and the back side should have a slogan and text indicating that we offer services on anything including cars, trucks, motorcycles and RVs. slogan will read "we take pride in your ride"
maybe also very small on the back side the IG icon with Brenners_Detail_Shop

phone 482.615.7734
address 7384 E Harlow Ave
Spokane WA 99342
email: BrennersDetail@quorvail.com

Target Market(s)

all ages , auto enthusiasts

Industry/Entity Type

Automotive

Contact Information for Business Card

the front should have logo, address, phone and email and the back side should have a slogan and text indicating that we offer services on anything including cars, trucks, motorcycles and RVs. slogan will read "we take pride in your ride"

phone 482.615.7734
address 7384 E Harlow Ave
Spokane WA 99342

Colors
000000
ffffff

Requirements
Must have
• bold font and very simple design with good spacing
Nice to have
• anything creative from the designer indicating we service any types of vehicles
Should not have
• any colors ,

```html
<!DOCTYPE html>
<html lang="en">
<head>
<meta charset="utf-8">
<title>Brenner's Detail Shop – Business Card</title>
<link rel="stylesheet" href="https://fonts.googleapis.com/css2?family=Arvo:wght@400;700&display=swap">
<style>
  :root {
    --backdrop: #9a9a9a;
    --ink: #000000;
    --card-dark: #1b1b1b;
    --card-light: #ffffff;
    --text-light: #ffffff;
    --ghost: #262626;
    --rule: #333333;
  }
  * { margin: 0; padding: 0; box-sizing: border-box; }
  html, body {
    width: 1200px; height: 1000px; overflow: hidden;
    background: var(--backdrop);
    font-family: "Arvo", "Rockwell", serif;
  }
  .card {
    position: absolute;
    top: 209px;
    width: 352px;
    height: 586px;
  }
  /* Back side */
  .card--back {
    left: 215px;
    background: var(--card-dark);
    color: var(--text-light);
    text-align: center;
  }
  .ghost-name {
    position: absolute;
    left: 0; right: 0; top: 300px;
    font-weight: 700;
    font-size: 40px;
    line-height: 1.05;
    color: var(--ghost);
  }
  .slogan {
    position: absolute;
    left: 0; right: 0; top: 263px;
    font-weight: 700;
    font-size: 23px;
    line-height: 30px;
    letter-spacing: 0.3px;
  }
  .services-label {
    position: absolute;
    left: 0; right: 0; top: 452px;
    font-size: 12px;
    letter-spacing: 0.6px;
  }
  .services-list {
    position: absolute;
    left: 0; right: 0; top: 472px;
    font-weight: 700;
    font-size: 15px;
    line-height: 23px;
    letter-spacing: 0.6px;
  }
  .services-list small { font-size: 9px; }
  .social-mark {
    position: absolute;
    left: 166px; top: 531px;
  }
  /* Front side */
  .card--front {
    left: 648px;
    background: var(--card-light);
    color: var(--ink);
  }
  .contact {
    position: absolute;
    left: 35px; top: 34px;
    font-weight: 700;
    font-size: 15px;
    line-height: 19px;
    letter-spacing: 0.4px;
  }
  .contact__item { display: block; }
  .contact__rule {
    height: 2px;
    width: 205px;
    margin: 11px 0 12px -2px;
    background: linear-gradient(90deg, var(--rule), rgba(0,0,0,0));
  }
  .brand {
    position: absolute;
    left: 130px; top: 418px;
    width: 200px;
    text-align: center;
    font-weight: 700;
    font-size: 30px;
    line-height: 1.1;
    color: var(--ink);
  }
  .brand__dot {
    display: block;
    width: 16px; height: 16px;
    margin: 0 auto 10px;
    border-radius: 50%;
    background: var(--ink);
  }
</style>
</head>
<body>
  <section class="card card--back" aria-label="Card back">
    <div class="ghost-name" aria-hidden="true">Brenner's<br>Detail Shop</div>
    <h2 class="slogan">WE TAKE PRIDE<br>IN YOUR RIDE</h2>
    <p class="services-label">SERVICES OFFERED ON:</p>
    <p class="services-list">CARS &nbsp;•&nbsp; TRUCKS<br>MOTORCYCLE &nbsp;•&nbsp; SRV<small>s</small></p>
    <svg class="social-mark" width="20" height="20" viewBox="0 0 20 20" aria-label="Social profile Brenners_Detail_Shop" role="img">
      <circle cx="10" cy="10" r="8.5" fill="none" stroke="#ffffff" stroke-width="2"/>
    </svg>
  </section>

  <section class="card card--front" aria-label="Card front">
    <div class="contact">
      <span class="contact__item">7384 E Harlow Ave</span>
      <span class="contact__item">Spokane WA 99342</span>
      <div class="contact__rule"></div>
      <span class="contact__item">482.615.7734</span>
      <div class="contact__rule"></div>
      <span class="contact__item">BrennersDetail@quorvail.com</span>
    </div>
    <div class="brand">
      <span class="brand__dot"></span>
      Brenner's<br>Detail Shop
    </div>
  </section>
</body>
</html>
```